Used Semi Truck Website Redesign

We are redoing the website backend and would like to also do a front end redesign. I would like a Mobile and Desktop mockup for each page. The website has more mobile visitors than desktop visitors. Our competitor is http://www.haulmarketbay.example. We don't want to copy them exactly but we want a site that looks more like that. We need the functionality of that site. One big difference is that we also sell parts and trailers.

We need a redesign for front page, product detail page, search result page, content page. It is very important that the site is very easy to use on mobile devices. Our target audience is Truck drivers.

Feel free to use demo fonts stock images, and icons. We will purchase necessary 3rd party media when a winner is chosen.

Target Market(s)

People who want to buy used trucks.

Coding

Coded - Design and coding required

Number of Pages Required

5+ page

Requirements
Must have
• Mockup for Desktop and Mobile pages.

```html
<!DOCTYPE html>
<html lang="en">
<head>
<meta charset="utf-8">
<title>Truck Search Results</title>
<link rel="stylesheet" href="https://fonts.googleapis.com/css2?family=Roboto:wght@300;400;500;700&display=swap">
<style>
:root{
  --red:#e8232b;
  --red-dark:#c4161d;
  --ink:#222;
  --text:#555;
  --muted:#999;
  --line:#e4e4e4;
  --page:#efefef;
  --white:#fff;
  --dark:#1f2126;
}
*{box-sizing:border-box;margin:0;padding:0}
html,body{width:1200px;height:2360px;overflow:hidden}
body{font-family:'Roboto',Arial,sans-serif;background:var(--page);color:var(--text);position:relative}
.hero{position:absolute;left:0;top:0;width:1200px;height:345px;background:linear-gradient(180deg,#2a2d33 0%,#3a3e46 45%,#23252a 100%)}
.topbar{position:absolute;left:0;top:0;width:1200px;height:40px;display:flex;align-items:center;padding:0 40px}
.brand{font-size:18px;font-weight:700;color:var(--white)}
.brand span{color:var(--red)}
.nav{position:absolute;left:440px;top:13px;display:flex;gap:30px;font-size:12px;color:#ddd}
.nav a{color:inherit;text-decoration:none}
.nav a.active{color:var(--white);font-weight:500}
.social{position:absolute;right:30px;top:12px;display:flex;gap:12px}
.social i{display:block;width:14px;height:14px;border-radius:50%;background:#cfcfcf}
.headline{position:absolute;top:222px;width:1200px;text-align:center;color:var(--white);font-size:26px;font-weight:500}
.tabs{position:absolute;top:264px;left:0;width:1200px;display:flex;justify-content:center;gap:10px}
.tabs span{display:block;padding:9px 18px;background:var(--white);color:var(--ink);font-size:12px;font-weight:500;border-radius:2px}
.tabs span.on{background:var(--red);color:var(--white)}
.searchbar{position:absolute;top:345px;left:0;width:1200px;height:72px;background:var(--red);display:flex;align-items:center;padding:0 88px;gap:0}
.searchbar .field{flex:1;height:40px;display:flex;align-items:center;justify-content:space-between;padding:0 22px 0 0;color:var(--white);font-size:12px;border-right:1px solid rgba(255,255,255,.25);margin-right:18px}
.searchbar .go{width:56px;height:72px;background:var(--red-dark);display:flex;align-items:center;justify-content:center}
.results{position:absolute;left:88px;top:460px;width:632px}
.card{background:var(--white);height:300px;margin-bottom:30px;padding:16px;display:flex;gap:20px}
.photo{width:240px;height:268px;flex:none}
.info{padding-top:10px}
.info h3{font-size:17px;font-weight:500;color:var(--ink)}
.price{font-size:17px;color:var(--ink);margin-top:6px}
.meta{display:flex;gap:24px;font-size:11px;color:var(--muted);margin-top:18px}
.meta b{color:var(--ink);font-weight:500}
.desc{font-size:11px;line-height:17px;color:var(--muted);margin-top:12px;width:330px}
.btn{display:inline-block;margin-top:18px;background:var(--dark);color:var(--white);font-size:11px;padding:10px 16px;border-radius:2px}
.actions{display:flex;gap:24px;margin-top:18px;font-size:11px;color:var(--muted);align-items:center}
.actions span{display:flex;align-items:center;gap:6px}
.box{width:11px;height:11px;border:1px solid #bbb}
.sidebar{position:absolute;left:740px;top:460px;width:372px;background:var(--white)}
.side-head{background:var(--red);height:60px;display:flex;align-items:center;justify-content:space-between;padding:0 18px;color:var(--white)}
.side-head h2{font-size:17px;font-weight:500}
.side-head small{font-size:11px}
.filter{border-bottom:1px solid var(--line);padding:18px 18px;font-size:12px;color:var(--ink)}
.filter .row{display:flex;justify-content:space-between;align-items:center}
.filter .chev{width:8px;height:8px;border-right:1.5px solid #999;border-bottom:1.5px solid #999;transform:rotate(45deg)}
.input{margin-top:12px;height:32px;border:1px solid var(--line);font-size:11px;color:var(--muted);display:flex;align-items:center;padding:0 10px}
.pair{display:flex;gap:10px;margin-top:12px}
.pair .input{margin-top:0;flex:1}
.opts{display:flex;gap:26px;margin-top:12px;font-size:11px;color:var(--text);align-items:center}
.opts span{display:flex;align-items:center;gap:6px}
.dot{width:10px;height:10px;border-radius:50%;border:1px solid #bbb}
.dot.on,.box.on{background:var(--red);border-color:var(--red)}
.collapsed{padding:20px 18px}
</style>
</head>
<body>
<header class="hero" role="img" aria-label="Dark photo of semi trucks parked at dusk">
  <div class="topbar"><div class="brand">Logo <span>Here</span></div></div>
  <nav class="nav"><a class="active">Login</a><a>Register</a><a>Find a Dealer</a><a>Dealer Login</a></nav>
  <div class="social"><i></i><i></i><i></i><i></i><i></i></div>
  <h1 class="headline">256,140 trucks and trailers for sale</h1>
  <div class="tabs"><span>Find</span><span class="on">Sell</span><span>Research</span></div>
</header>

<form class="searchbar">
  <div class="field">Keywords</div>
  <div class="field">Select a class <span>▾</span></div>
  <div class="field">Select a category <span>▾</span></div>
  <div class="field">Zip code</div>
  <div class="field">Any Distance <span>▾</span></div>
  <div class="go"><svg width="18" height="18" viewBox="0 0 18 18"><circle cx="7.5" cy="7.5" r="5.5" fill="none" stroke="#fff" stroke-width="2"/><line x1="11.5" y1="11.5" x2="16" y2="16" stroke="#fff" stroke-width="2"/></svg></div>
</form>

<main class="results">
  <article class="card">
    <div class="photo" role="img" aria-label="Work truck on a construction site with traffic cones" style="background:linear-gradient(160deg,#c9cdd2,#6d6f6a 60%,#9a5b2e)"></div>
    <div class="info">
      <h3>2018 Company name, Truck/Trailer name</h3>
      <div class="price">$29,000</div>
      <div class="meta"><span>Condition: <b>New</b></span><span>Location: <b>Birmingham, AL</b></span></div>
      <p class="desc">Aenean vulputate eleifend tellus aenean leo ligula porttitor eu consequat vitae eleifend ac enim aliquam lorem ante dapibus in.</p>
      <span class="btn">More Details</span>
      <div class="actions"><span><i class="box"></i>Compare</span><span>♡ Save</span></div>
    </div>
  </article>
  <article class="card">
    <div class="photo" role="img" aria-label="Semi truck on an open road under a dark sky" style="background:linear-gradient(180deg,#2c2f33,#55585c 55%,#8a8a86)"></div>
    <div class="info">
      <h3>2018 Company name, Truck/Trailer name</h3>
      <div class="price">$29,000</div>
      <div class="meta"><span>Condition: <b>New</b></span><span>Location: <b>Birmingham, AL</b></span></div>
      <p class="desc">Aenean vulputate eleifend tellus aenean leo ligula porttitor eu consequat vitae eleifend ac enim aliquam lorem ante dapibus in.</p>
      <span class="btn">More Details</span>
      <div class="actions"><span><i class="box"></i>Compare</span><span>♡ Save</span></div>
    </div>
  </article>
  <article class="card">
    <div class="photo" role="img" aria-label="White semi truck on a highway under a blue sky" style="background:linear-gradient(180deg,#8fb3d4,#d7dde2 55%,#7b7f82)"></div>
    <div class="info">
      <h3>2018 Company name, Truck/Trailer name</h3>
      <div class="price">$29,000</div>
      <div class="meta"><span>Condition: <b>New</b></span><span>Location: <b>Birmingham, AL</b></span></div>
      <p class="desc">Aenean vulputate eleifend tellus aenean leo ligula porttitor eu consequat vitae eleifend ac enim aliquam lorem ante dapibus in.</p>
      <span class="btn">More Details</span>
      <div class="actions"><span><i class="box"></i>Compare</span><span>♡ Save</span></div>
    </div>
  </article>
  <article class="card">
    <div class="photo" role="img" aria-label="Yellow concrete mixer truck at a sandy work site" style="background:linear-gradient(180deg,#a9c3da,#c9b47a 55%,#9c8655)"></div>
    <div class="info">
      <h3>2018 Company name, Truck/Trailer name</h3>
      <div class="price">$29,000</div>
      <div class="meta"><span>Condition: <b>New</b></span><span>Location: <b>Birmingham, AL</b></span></div>
      <p class="desc">Aenean vulputate eleifend tellus aenean leo ligula porttitor eu consequat vitae eleifend ac enim aliquam lorem ante dapibus in.</p>
      <span class="btn">More Details</span>
      <div class="actions"><span><i class="box"></i>Compare</span><span>♡ Save</span></div>
    </div>
  </article>
  <article class="card">
    <div class="photo" role="img" aria-label="Row of parked semi trucks at a truck stop" style="background:linear-gradient(180deg,#b9cde0,#d4d6d8 50%,#6a6c6f)"></div>
    <div class="info">
      <h3>2018 Company name, Truck/Trailer name</h3>
      <div class="price">$29,000</div>
      <div class="meta"><span>Condition: <b>New</b></span><span>Location: <b>Birmingham, AL</b></span></div>
      <p class="desc">Aenean vulputate eleifend tellus aenean leo ligula porttitor eu consequat vitae eleifend ac enim aliquam lorem ante dapibus in.</p>
      <span class="btn">More Details</span>
      <div class="actions"><span><i class="box"></i>Compare</span><span>♡ Save</span></div>
    </div>
  </article>
</main>

<aside class="sidebar">
  <div class="side-head"><h2>Refine Search</h2><small>✕ Remove all filters</small></div>
  <div class="filter"><div class="row">Keyword<i class="chev"></i></div><div class="input">Enter keyword</div></div>
  <div class="filter"><div class="row">Location<i class="chev"></i></div>
    <div class="opts"><span><i class="dot on"></i>Use</span><span><i class="dot"></i>20 Miles</span></div>
    <div class="pair"><div class="input">Enter zip code</div><div class="input" style="flex:none;width:60px">Go</div></div></div>
  <div class="filter"><div class="row">Condition<i class="chev"></i></div>
    <div class="opts"><span><i class="box on"></i>New (12,042)</span><span><i class="box"></i>Used (48,220)</span></div></div>
  <div class="filter"><div class="row">Mileage<i class="chev"></i></div><div class="pair"><div class="input">From</div><div class="input">To</div></div></div>
  <div class="filter"><div class="row">Model years<i class="chev"></i></div><div class="pair"><div class="input">From</div><div class="input">To</div></div></div>
  <div class="filter"><div class="row">Location<i class="chev"></i></div>
    <div class="opts"><span><i class="dot on"></i>Accepting Offers</span><span><i class="dot"></i>Firm price</span></div></div>
  <div class="filter collapsed"><div class="row">Class<i class="chev"></i></div></div>
  <div class="filter collapsed"><div class="row">Category<i class="chev"></i></div></div>
  <div class="filter collapsed"><div class="row">Truck Manufacturer<i class="chev"></i></div></div>
  <div class="filter collapsed"><div class="row">Upfit Manufacturer<i class="chev"></i></div></div>
  <div class="filter collapsed"><div class="row">Upfit Body Type<i class="chev"></i></div></div>
  <div class="filter collapsed"><div class="row">Cab Type<i class="chev"></i></div></div>
  <div class="filter collapsed"><div class="row">Engine<i class="chev"></i></div></div>
  <div class="filter collapsed"><div class="row">Drivetrain<i class="chev"></i></div></div>
  <div class="filter collapsed"><div class="row">Engine Type<i class="chev"></i></div></div>
  <div class="filter collapsed"><div class="row">Transmission Speed<i class="chev"></i></div></div>
  <div class="filter collapsed"><div class="row">Fuel Type<i class="chev"></i></div></div>
</aside>
</body>
</html>
```